Redesign existing website

We would like a redesign of the website http://www.velbrisanalytics.com that creates a more modern, up to date look.

Velbris Analytics creates software for social science research and is focused on making the software user friendly and easy to use. We would like to convey seriousness, but also
a very up to date, just released look.

Feel free to modify the logo if you wish.

Target Market(s)

Academics, researchers

Industry/Entity Type

Software

Requirements
Must have
• The design should incorporate the same information as the current website.

```html
<!DOCTYPE html>
<html lang="en">
<head>
<meta charset="utf-8">
<title>Velbris Analytics — Empowering the social science researcher</title>
<link href="https://fonts.googleapis.com/css2?family=PT+Sans:wght@400;700&family=Ropa+Sans&family=Raleway:wght@200&family=Arimo&display=swap" rel="stylesheet">
<style>
:root{
  --topbar-dark:#3e3e3e;
  --brand-blue:#233c9a;
  --nav-blue:#1f3d9c;
  --text-grey:#666;
  --body-grey:#555;
  --hero-yellow:#ffd200;
  --hero-pale:#ffe98a;
  --gold:#b8960a;
  --footer:#3b3b3b;
  --footer-text:#9a9a9a;
  --bottom:#262626;
  --link-blue:#3f63c8;
}
*{margin:0;padding:0;box-sizing:border-box}
html,body{width:1200px;height:1200px;overflow:hidden;background:var(--bottom)}
body{font-family:"PT Sans",sans-serif;position:relative}
.topbar{position:absolute;left:0;top:0;width:1200px;height:40px;background:linear-gradient(#5a5a5a,var(--topbar-dark));border-bottom:2px solid #222}
.account{position:absolute;right:120px;top:11px;font-size:12px;color:#eee;display:flex;gap:18px}
.account span+span{border-left:1px solid #ccc;padding-left:18px}
.header{position:absolute;left:0;top:42px;width:1200px;height:173px;background:#fff}
.logo{position:absolute;left:120px;top:18px;display:flex;flex-direction:column;align-items:flex-start}
.logo-mark{width:72px;height:72px;border-radius:50%;background:var(--brand-blue);margin-left:52px;border:4px solid #e4e4e4}
.logo-name{font-size:21px;font-weight:700;color:var(--brand-blue);margin-top:6px}
.tagline{position:absolute;left:122px;top:129px;font-size:14px;color:var(--text-grey);letter-spacing:.4px}
.nav{position:absolute;left:494px;top:22px;display:flex;font-size:12px;color:var(--text-grey)}
.nav a{color:inherit;text-decoration:none;padding:0 18px;border-left:1px solid #888;line-height:14px}
.nav a:first-child{border:0;padding-left:0;color:var(--nav-blue)}
.preview{position:absolute;left:875px;top:-2px;width:205px;height:65px;background:linear-gradient(#3a64d4,#1f3f9e);border-radius:0 0 8px 8px;box-shadow:2px 3px 4px rgba(0,0,0,.35);color:#fff;text-align:center;padding-top:12px}
.preview small{display:block;font-size:12px}
.preview strong{display:block;font-family:"Ropa Sans",sans-serif;font-weight:400;font-size:19px;margin-top:2px}
.hero{position:absolute;left:0;top:215px;width:1200px;height:367px;background:repeating-linear-gradient(90deg,#1a1a1a 0 3px,#232323 3px 5px,#161616 5px 8px)}
.hero-art{position:absolute;left:125px;top:40px;width:515px;height:327px;background:linear-gradient(160deg,#3d7f2a 0%,#8e8a2c 45%,#7a5a3e 80%,#3a2f28 100%)}
.hero-copy{position:absolute;left:774px;top:73px;font-family:"Ropa Sans",sans-serif;color:#fff;line-height:1.1}
.hero-copy .lead{font-size:26px}
.hero-copy .big{font-size:52px;color:var(--hero-yellow);margin-top:6px}
.hero-copy .sub{font-size:30px;color:var(--hero-pale)}
.main{position:absolute;left:0;top:582px;width:1200px;height:378px;background:#fff}
.welcome{position:absolute;left:121px;top:38px;font-family:"Raleway",sans-serif;font-weight:200;font-size:38px;color:var(--nav-blue);letter-spacing:-.5px}
.mission{position:absolute;left:121px;top:103px;width:965px;font-family:"Arimo",sans-serif;font-size:12px;line-height:14px;color:var(--body-grey);letter-spacing:-.15px}
.helps{position:absolute;left:121px;top:173px;font-size:13px;color:#444}
.helps em{font-style:normal;color:var(--gold)}
.features{position:absolute;left:150px;top:208px;list-style:none;font-size:12.5px;color:#2d3f7a;letter-spacing:-.1px}
.features li{display:flex;align-items:center;height:33px}
.features i{width:24px;height:20px;margin-right:20px;border-radius:3px;flex:none}
.divider{position:absolute;left:710px;top:180px;width:1px;height:170px;background:#ccc}
.pointer{position:absolute;left:711px;top:256px}
.download{position:absolute;left:737px;top:225px;width:323px;height:78px;border-radius:8px;background:linear-gradient(#2e2e2e,#000);box-shadow:3px 4px 5px rgba(0,0,0,.4);color:#ddd;font-size:17px;display:flex;align-items:center;padding-left:38px}
.download svg{margin-right:14px}
.download b{font-weight:400;color:#7aa0ff;margin-left:5px}
.footer{position:absolute;left:0;top:960px;width:1200px;height:180px;background:var(--footer);border-top:2px solid #222;border-bottom:2px solid #1a1a1a}
.f-logo{position:absolute;left:150px;top:14px;width:256px;text-align:center}
.f-logo .logo-mark{margin:0 auto;border-color:#ddd}
.f-logo .logo-name{font-size:21px;margin-top:4px;color:#4f6fd6}
.f-logo p{font-size:11px;color:#888;margin-top:10px;line-height:13px;letter-spacing:.3px}
.f-col{position:absolute;top:16px;font-size:11px;color:var(--footer-text)}
.f-col h4{font-size:12px;color:#eee;font-weight:400;letter-spacing:.5px;margin-bottom:8px}
.f-col li{list-style:none;height:24.3px;display:flex;align-items:center}
.f-col li i{width:15px;height:14px;margin-right:10px;border-radius:2px}
.f-rule{position:absolute;top:20px;width:1px;height:145px;background:#2b2b2b;border-right:1px solid #4a4a4a}
.bottom{position:absolute;left:0;top:1142px;width:1200px;height:58px;background:var(--bottom);font-size:11px;color:#999}
.bottom .copy{position:absolute;left:149px;top:15px;letter-spacing:.3px}
.bottom .legal{position:absolute;right:148px;top:15px;color:var(--link-blue)}
.bottom .legal span+span{border-left:1px solid #888;margin-left:6px;padding-left:8px}
</style>
</head>
<body>
<div class="topbar"><div class="account"><span>Login</span><span>Register</span></div></div>

<header class="header">
  <div class="logo"><div class="logo-mark"></div><div class="logo-name">Velbris Analytics</div></div>
  <div class="tagline">Empowering the social science researcher</div>
  <nav class="nav"><a href="#">Home</a><a href="#">Products</a><a href="#">News</a><a href="#">About Us</a><a href="#">Contact Us</a></nav>
  <div class="preview"><small>Download Preview Release</small><strong>VELBRIS DATA MANAGER</strong></div>
</header>

<section class="hero">
  <div class="hero-art" role="img" aria-label="Photo of an open hand holding a glossy 3D pie chart"></div>
  <div class="hero-copy">
    <div class="lead">Increasing The Power And<br>Efficiency Of Empirical</div>
    <div class="big">Social Science</div>
    <div class="sub">RESEARCHER</div>
  </div>
</section>

<main class="main">
  <h1 class="welcome">WELCOME</h1>
  <p class="mission">The mission of Velbris Analytics, Inc. is to produce software products that multiply the power and efficiency of empirical scientific research in the social sciences. A central goal is to expand access to complex data sources and to the advanced methods of scientific investigation needed to analyze them. Reliance on antiquated data management tools imposes heavy costs on the research community. The VDM reduces the costs of research by allowing analysts to manipulate data without the assistance of professional programming staff.</p>
  <div class="helps">THE <em>VELBRIS DATA MANAGER (VDM)</em> HELPS RESEARCHERS:</div>
  <ul class="features">
    <li><i style="background:#e8c24a"></i>Integrate data from different periods, places, and sources</li>
    <li><i style="background:linear-gradient(90deg,#7bc043 33%,#f2b632 33% 66%,#e86a2a 66%)"></i>Restructure complex data structures for analysis</li>
    <li><i style="background:#4aa0d8;border-radius:50%"></i>Generate simple descriptive statistics for diagnostic purposes and feasibility analyses</li>
    <li><i style="background:#eef0f4;border:1px solid #bbb"></i>Export subsets of variables and cases in formats suitable for analysis in any statistical package.</li>
  </ul>
  <div class="divider"></div>
  <svg class="pointer" width="12" height="16"><path d="M0 0 L12 8 L0 16Z" fill="#ccc"/></svg>
  <div class="download">
    <svg width="24" height="32"><path d="M7 0h10v16h7L12 32 0 16h7z" fill="#2f6fe0"/></svg>
    Download<b>Velbris Data Manager</b>
  </div>
</main>

<footer class="footer">
  <div class="f-logo">
    <div class="logo-mark"></div>
    <div class="logo-name">Velbris Analytics</div>
    <p>Increasing The Power And Efficiency Of Empirical<br>Social Science Research</p>
  </div>
  <div class="f-rule" style="left:510px;top:65px;height:115px"></div>
  <div class="f-col" style="left:549px"><h4>SITE LINKS</h4><ul><li>Home</li><li>Products</li><li>News</li><li>About Us</li><li>Contact Us</li></ul></div>
  <div class="f-rule" style="left:675px"></div>
  <div class="f-col" style="left:752px"><h4>PRODUCTS</h4><ul><li>Overview</li><li>Features</li><li>Datasets</li><li>Screenshots</li><li>Support</li></ul></div>
  <div class="f-rule" style="left:877px"></div>
  <div class="f-col" style="left:952px"><h4>CONNECT WITH US</h4><ul>
    <li><i style="background:#5fb7e4"></i>Chatter</li>
    <li><i style="background:#3b5ba0"></i>Friendbook</li>
    <li><i style="background:#d9d9d9"></i>Clipstream</li>
    <li><i style="background:#f08a24"></i>Rss Feed</li>
    <li><i style="background:#cfe0f2"></i>Email</li>
  </ul></div>
</footer>

<div class="bottom">
  <div class="copy">Copyright © Velbris Analytics 2011. All Rights Reserved.</div>
  <div class="legal"><span>Privacy Policy</span><span>Disclaimer</span></div>
</div>
</body>
</html>
```